Risk Management Company in need of Business Card Design

We sell risk management insurance to Lenders (Banks, Credit Unions, Real Estate Trust).

We need a very clean, professional card that will leave a great impression.

We are looking to use a blue color for our logo on the card (Preferably close to royal blue but are open to looking at navy blue or any darker blues as well).

Please see the logo attached to get an idea. We are open to writing Harbor Vault Under the logo or next to the logo. Really whatever looks best.

Target Market(s)

Banks, Credit Unions, Real Estate Trusts

Industry/Entity Type

Insurance

Contact Information for Business Card

Name: Mark Dunstan
Title: Regional Sales Director
Email: mdunstan@harborvault-example.net
C:555-318-2047
D:555-674-1192
800-555-0147 Ext.312
F:555-829-6630 (We would like to see some cards without the fax number as well to compare)

Company Name: Harbor Vault
Website: www.harborvault-example.net

Address: 418 E. Marlowe St. Suite 140, Towson, MD 21286 (Preferably written on the bottom of the card in small print.)

Colors
0355a3
0455a3

Requirements
Nice to have
• We would like to see a couple of where the back has the logo in reverse colors (Logo White, Background Blue)

```html
<!DOCTYPE html>
<html lang="en">
<head>
<meta charset="utf-8">
<title>Harbor Vault — Business Card</title>
<link rel="stylesheet" href="https://fonts.googleapis.com/css2?family=EB+Garamond:wght@400;500&display=swap">
<style>
  :root {
    --navy: #23225f;
    --paper: #ffffff;
    --backdrop: #e9e7e3;
    --shadow: rgba(0, 0, 0, 0.28);
  }
  * { margin: 0; padding: 0; box-sizing: border-box; }
  html, body {
    width: 1200px; height: 800px; overflow: hidden;
    background: var(--backdrop);
    font-family: "EB Garamond", Georgia, serif;
    color: var(--navy);
  }
  .canvas { position: relative; width: 1200px; height: 800px; }

  .card {
    position: absolute;
    background: var(--paper);
    box-shadow: 2px 3px 6px var(--shadow);
    overflow: hidden;
  }

  /* Front side: reversed colours */
  .card--front { left: 72px; top: 38px; width: 585px; height: 338px; }
  .card--front .field {
    position: absolute; left: 0; right: 0; top: 22px; bottom: 23px;
    background: var(--navy); color: var(--paper); text-align: center;
  }
  .card--front .brand-mark {
    position: absolute; left: 257px; top: 95px;
    width: 70px; height: 70px; background: var(--paper);
  }
  .card--front .brand-name {
    position: absolute; left: 0; right: 0; top: 195px;
    font-size: 25px; letter-spacing: 0.3px;
  }
  .card--front .website {
    position: absolute; left: 0; right: 0; top: 265px;
    font-size: 16px;
  }

  /* Back side: contact details */
  .card--back { left: 553px; top: 409px; width: 587px; height: 343px; }
  .card--back .band { position: absolute; left: 0; right: 0; height: 23px; background: var(--navy); }
  .card--back .band--top { top: 0; }
  .card--back .band--bottom { bottom: 0; height: 24px; }

  .card--back .brand-mark {
    position: absolute; left: 73px; top: 90px;
    width: 85px; height: 85px; background: var(--navy);
  }
  .card--back .brand-name {
    position: absolute; left: 15px; width: 200px; top: 240px;
    text-align: center; font-size: 25px;
  }

  .holder {
    position: absolute; right: 27px; top: 40px; text-align: center; width: 260px;
  }
  .holder .person { font-size: 29px; letter-spacing: 3px; font-weight: 400; white-space: nowrap; }
  .holder .role { font-size: 14px; margin-top: 6px; }

  .address {
    position: absolute; left: 391px; top: 152px;
    font-size: 13px; line-height: 16px; font-style: normal; white-space: nowrap;
  }

  .contact { position: absolute; left: 356px; list-style: none; }
  .contact li { display: flex; align-items: flex-start; font-size: 13.5px; white-space: nowrap; }
  .contact svg { width: 20px; height: 16px; margin-right: 8px; margin-top: 2px; flex: none; }
  .contact--email { top: 192px; }
  .contact--web { top: 216px; }
  .contact--phone { top: 242px; }
  .phones { line-height: 17px; font-size: 14px; }
</style>
</head>
<body>
<main class="canvas">

  <section class="card card--front" aria-label="Card front">
    <div class="field">
      <div class="brand-mark"></div>
      <p class="brand-name">Harbor Vault</p>
      <p class="website">www.harborvault-example.net</p>
    </div>
  </section>

  <section class="card card--back" aria-label="Card back">
    <div class="band band--top"></div>

    <div class="brand-mark"></div>
    <p class="brand-name">Harbor Vault</p>

    <header class="holder">
      <h1 class="person">Mark Dunstan</h1>
      <p class="role">Regional Sales Director</p>
    </header>

    <address class="address">
      418 E. Marlowe St. Suite<br>140, Towson, MD 21286
    </address>

    <ul class="contact contact--email">
      <li>
        <svg viewBox="0 0 20 16" aria-hidden="true"><rect x="1" y="2" width="18" height="12" fill="none" stroke="#23225f" stroke-width="1.6"/><path d="M1 2 L10 9 L19 2" fill="none" stroke="#23225f" stroke-width="1.6"/></svg>
        <span>mdunstan@harborvault-example.net</span>
      </li>
    </ul>
    <ul class="contact contact--web">
      <li>
        <svg viewBox="0 0 20 16" aria-hidden="true"><g fill="none" stroke="#23225f" stroke-width="1.3"><circle cx="10" cy="8" r="7"/><ellipse cx="10" cy="8" rx="3" ry="7"/><path d="M3 8 H17 M4.5 4 H15.5 M4.5 12 H15.5"/></g></svg>
        <span>www.harborvault-example.net</span>
      </li>
    </ul>
    <ul class="contact contact--phone">
      <li>
        <svg viewBox="0 0 20 16" aria-hidden="true"><rect x="3" y="0" width="14" height="16" rx="2" fill="#23225f"/><path d="M7.5 3.5 C6.5 4.5 7 8 9.5 10.5 C11 12 12.5 12.5 13 12 L13.5 11 L11.8 9.6 L10.9 10.3 C10 9.6 9 8.4 8.6 7.3 L9.4 6.6 L8.5 4.5 Z" fill="#ffffff"/></svg>
        <span class="phones">555-318-2047<br>555-674-1192<br>800-555-0147<br>Ext.312</span>
      </li>
    </ul>

    <div class="band band--bottom"></div>
  </section>

</main>
</body>
</html>
```